Task Description:
I’m wanting a professionally designed 8 ½' x 11, 3 fold brochure, both sides, to print as my target audience are those people who primarily don’t have access to the internet. These items will be dropped off in the mailboxes of all households in the city.
However I do have a web site www.brightcivicpath.ca where I would like to have it as a document that can be down loaded.
This is my first foray into political office and my message needs to be clear, concise and easy to understand. The brochure should be a bit conservative yet be warm and inviting. I’ve selected two pictures that I think make sense under their respective headings, but I'm open to suggestions.I need to update my picture for the front cover.
There is the possibility of having T shirts and business cards made up, which would be in essence a simpler version of the brochure so please keep this in mind. I ask that you work with me and I will compensate you accordingly for the extras should they be required. You may want to consider making the Bright Civic Path into a logo as we own all the web extensions and have applied for copyright protection for branding purposes.
You may want to look at QM Larchfield http://www.qmlarchfield.ca/ , or the Pinecrest Bank of Canada www.pinecrestbank.com as two recognizable colour schemes here in Canada but don’t let that limit your imagination.
The content in the flier should remain intact although I am open to some minor suggestions. As you can see my talents as a graphic artist are limited hence my need for that professional make over that will give it a bit of razzle dazzle and set me out from the other candidates. So use your imagination!!
Target Market(s)
Middle age voters who may or may not have access to the internet and still prefer print
Industry/Entity Type
Conservative

```html
<!DOCTYPE html>
<html lang="en">
<head>
<meta charset="utf-8">
<title>Reid Colton for Mayor – Brochure Panel</title>
<link href="https://fonts.googleapis.com/css2?family=Archivo+Black&family=PT+Sans:wght@400;700&display=swap" rel="stylesheet">
<style>
  :root {
    --brand-blue: #3a5bf0;
    --deep-blue: #1c2fd6;
    --ink: #16166e;
    --headline-black: #0d0d0d;
    --sky-top: #c9d4fb;
    --sky-mid: #e6e8f5;
    --sand: #ddd0c3;
    --white: #ffffff;
  }
  * { margin: 0; padding: 0; box-sizing: border-box; }
  html, body { width: 1200px; height: 908px; overflow: hidden; background: var(--white); }
  .brochure {
    position: relative; width: 1200px; height: 908px; overflow: hidden;
    background: linear-gradient(180deg, var(--sky-top) 110px, var(--sky-mid) 330px, #ece4dc 560px, var(--sand) 760px, #e8e0d8 850px);
    font-family: "PT Sans", Arial, sans-serif; color: var(--ink);
  }
  .masthead {
    position: absolute; left: 0; top: 0; width: 1200px; height: 102px; background: var(--brand-blue);
  }
  .masthead-rule {
    position: absolute; left: 0; top: 109px; width: 1200px; height: 9px; background: var(--brand-blue);
  }
  .footer-rule {
    position: absolute; left: 0; top: 852px; width: 1200px; height: 5px; background: var(--deep-blue);
  }
  .footer-band {
    position: absolute; left: 0; top: 861px; width: 1200px; height: 47px; background: var(--brand-blue);
  }
  .panel-title {
    position: absolute; font-family: "Archivo Black", Arial, sans-serif; color: var(--white);
    font-size: 31px; line-height: 39px;
  }
  .panel-title.inside { left: 57px; top: 10px; }
  .panel-title.vote { left: 455px; width: 290px; top: 13px; text-align: center; }
  .tagline {
    position: absolute; left: 905px; top: 23px; width: 200px; text-align: center;
    color: var(--white); font-weight: 700; line-height: 16px;
  }
  .tagline span { display: block; font-size: 10.5px; }
  .tagline span.big { font-size: 12.5px; }
  .tagline span.bigger { font-size: 13.5px; }
  .column {
    position: absolute; font-size: 15px; line-height: 19.8px; text-align: justify;
  }
  .column p { margin-bottom: 19.8px; }
  .column strong { font-weight: 700; }
  .column .name { font-size: 18px; }
  .column.story { left: 55px; top: 142px; width: 296px; }
  .column.business { left: 455px; top: 142px; width: 297px; text-indent: 30px; }
  .column.plan { left: 462px; top: 558px; width: 296px; }
  .gap { height: 19.8px; }
  .photo-frame {
    position: absolute; left: 459px; top: 322px; width: 287px; height: 215px; background: var(--white);
    padding: 7px;
  }
  .photo-fill { width: 100%; height: 100%; }
  .bus-photo { background: linear-gradient(180deg, #4f8fe6 0%, #a9c9ef 40%, #d9dde2 58%, #6d6a62 78%, #4a4943 100%); }
  .vote-call {
    position: absolute; left: 455px; top: 742px; width: 297px; text-align: center;
    font-family: "Archivo Black", Arial, sans-serif; line-height: 28px;
  }
  .vote-call .date { font-size: 25px; color: #0f1780; }
  .vote-call .verb { font-size: 22px; color: #0f1780; }
  .vote-call .who { font-size: 22px; color: var(--brand-blue); }
  .cover-name {
    position: absolute; left: 880px; width: 260px; text-align: center; font-family: "Archivo Black", Arial, sans-serif;
    line-height: 1;
  }
  .cover-name.first { top: 138px; font-size: 54px; color: var(--headline-black); }
  .cover-name.last { top: 196px; font-size: 54px; color: var(--brand-blue); letter-spacing: 1px; }
  .portrait {
    position: absolute; left: 911px; top: 267px; width: 204px; height: 285px;
    background: linear-gradient(180deg, #d8d8d2 0%, #9a9a96 45%, #3a3a38 100%);
  }
  .cover-slogan {
    position: absolute; left: 870px; width: 280px; text-align: center; font-family: "Archivo Black", Arial, sans-serif; line-height: 1;
  }
  .cover-slogan.top { top: 589px; font-size: 34px; color: var(--headline-black); }
  .cover-slogan.bottom { top: 630px; font-size: 50px; color: var(--brand-blue); }
  .site-url {
    position: absolute; top: 873px; width: 400px; text-align: center; color: var(--white);
    font-family: "PT Sans", Arial, sans-serif; font-weight: 700; font-size: 19px; letter-spacing: 0.3px;
  }
  .site-url.left { left: 10px; }
  .site-url.middle { left: 406px; }
  .site-url.right { left: 809px; }
</style>
</head>
<body>
<main class="brochure">
  <header class="masthead"></header>
  <div class="masthead-rule"></div>

  <h1 class="panel-title inside">Getting to know<br>Bright Civic Path</h1>
  <h2 class="panel-title vote">Vote<br>Reid Colton</h2>
  <div class="tagline">
    <span>UNLOCK THE POTENTIAL</span>
    <span class="big">OF THE BEST SMALL CITY IN</span>
    <span class="bigger">NORTH AMERICA</span>
  </div>

  <section class="column story">
    <p><strong class="name">Reid Colton</strong> is a life long resident of Pine Harbour.</p>
    <p>&nbsp;My family has served this community and area for more than 100 years.</p>
    <div class="gap"></div>
    <p>&nbsp;- Samuel Colton built and managed the Harbour Grain Elevator.</p>
    <p>- Arthur Colton managed the Bayline Cement facility.</p>
    <p>-Ellen Colton was past president of the Chamber of Commerce.</p>
    <p>-Nora Colton is a gold medalist at the 2010 Winter Olympics.</p>
    <p>&nbsp;Although I have a unique vocation through the Safety Standards Guild (SSG) and could live and work anywhere in the world I have chosen to remain and work from Pine Harbour.</p>
    <p>&nbsp;On average I visit and work with more than 30 different corporations a year. I have a high pressure job as companies rely on my skills and expertise to keep them safe and operational. Solving problems, minimizing costs, maximizing production are challenges I face everyday.</p>
  </section>

  <section class="column business">
    <p>I’m currently involved with <strong>Voltrane Systems Inc</strong>. a newly created R&amp;D company developing electric propulsion systems for the transit industry. Our research partners consist of faculty and students from <strong>Northshore University.</strong> So I know first hand how difficult it is to start, finance and run a new business in this city.</p>
  </section>

  <figure class="photo-frame">
    <div class="photo-fill bus-photo" role="img" aria-label="Photo of an electric hybrid transit bus parked on a gravel lot"></div>
  </figure>

  <section class="column plan">
    <p>As <strong>Bright Civic Path,</strong> my goal is to be mayor for two terms, maximum three. With the implementation of a long term plan we will require a fresh face to step forward to complete the process. I also feel that we should reduce the number of city councilors and use those funds to make those positions full time. Term limits should apply to all elected positions!</p>
  </section>

  <div class="vote-call">
    <div class="date">On Oct 25th</div>
    <div class="verb">Vote</div>
    <div class="who">Reid Colton</div>
  </div>

  <div class="cover-name first">Reid</div>
  <div class="cover-name last">COLTON</div>
  <div class="portrait" role="img" aria-label="Black and white portrait photo of the candidate"></div>
  <div class="cover-slogan top">Bright Civic</div>
  <div class="cover-slogan bottom">PATH</div>

  <div class="footer-rule"></div>
  <footer class="footer-band"></footer>
  <div class="site-url left">www.brightcivicpath.ca</div>
  <div class="site-url middle">www.brightcivicpath.ca</div>
  <div class="site-url right">www.brightcivicpath.ca</div>
</main>
</body>
</html>
```